DL Flyer for conservation/restoration business

I am an objects conservator and run a business called FormKeep Conservation. I specialise in conserving and restoring 3 dimensional artworks and artefacts in Perth, Western Australia. I dont work on paintings, paper or textiles but pretty much everything else such as sculptures, metal, wood, ceramics etc. So far I have been reasonably successful in marketing to small museums and councils. However, I would like to pick up some more work from private individuals living in the more affluent areas of Perth.

I would like to have a DL flyer designed to do a letterbox drop in my target areas. I would like something professional and eyecatching that wont get thrown away. Also it will make the business look trustworthy.

I would like to have something that will go with my existing logo if possible.

Target Market(s)

wealthy individuals over 50 who enjoy collecting art / antiques

Industry/Entity Type

Marketing

Requirements
Must have
• I would like a good background image or images of suitable artworks/ artefacts/ conservator at work (hands only). Also include my logo as the business name.

I am happy to take advice on advertising, but my preference is for the text in the attached word file (order can be rearranged):

I would like to be able to edit the flyer if necessary at a later date, and would like it to be compatible with MS Publisher.
Should not have
• Do not include any images of paintings, textiles, paper or books.

```html
<!DOCTYPE html>
<html lang="en">
<head>
<meta charset="utf-8">
<title>FormKeep Conservation – DL Flyer</title>
<link href="https://fonts.googleapis.com/css2?family=Fira+Sans:wght@400;600&family=Arimo:ital,wght@1,700&display=swap" rel="stylesheet">
<style>
  :root {
    --red-top: #ff4d4d;
    --red-mid: #e00a0a;
    --red-deep: #a80000;
    --frame-line: rgba(255, 220, 220, 0.85);
    --text-light: #ffffff;
    --quote-fill: #fcd9c4;
    --quote-text: #1a1a1a;
    --bullet: #ffb3b3;
    --page: #ffffff;
  }
  * { box-sizing: border-box; margin: 0; padding: 0; }
  html, body { width: 1106px; height: 1200px; overflow: hidden; background: var(--page); }
  body { position: relative; font-family: "Fira Sans", Arial, sans-serif; color: var(--text-light); }

  .flyer-side {
    position: absolute;
    width: 527px; height: 1124px;
    background: linear-gradient(180deg, var(--red-top) 0%, var(--red-mid) 45%, var(--red-deep) 100%);
    box-shadow: 0 0 2px rgba(0,0,0,0.4);
    overflow: hidden;
  }
  .flyer-side--front { left: 14px; top: 18px; }
  .flyer-side--back  { left: 563px; top: 58px; }

  .trim-frame {
    position: absolute; left: 37px; top: 36px; width: 463px; height: 1045px;
    border: 1px solid var(--frame-line);
  }

  .brand {
    position: absolute; left: 88px; top: 86px;
    display: flex; align-items: center; gap: 16px;
  }
  .brand__mark { width: 56px; height: 56px; background: var(--text-light); flex: none; }
  .brand__name {
    font-weight: 600; font-size: 36px; line-height: 38px; color: var(--text-light);
  }
  .brand__name span { display: block; }

  .tagline {
    position: absolute; left: 177px; top: 304px;
    font-size: 20px; line-height: 23px; font-weight: 400;
  }
  .tagline span { display: block; }
  .tagline span + span { padding-left: 10px; }

  .credentials {
    position: absolute; left: 246px; top: 388px; width: 250px;
    font-family: "Arimo", Arial, sans-serif; font-style: italic; font-weight: 700;
    font-size: 18px; line-height: 22px;
  }

  .artefact { position: absolute; }
  .artefact--vase {
    left: 222px; top: 670px; width: 262px; height: 382px;
    background: radial-gradient(ellipse at 50% 45%, #4a2a1e 0%, #1e1512 60%, #120c0a 100%);
    border-radius: 42% 42% 30% 30% / 20% 20% 40% 40%;
  }
  .artefact--bust {
    left: 154px; top: 98px; width: 228px; height: 356px;
    background: radial-gradient(ellipse at 45% 40%, #8a4a38 0%, #4d2419 55%, #2a120c 100%);
    border-radius: 48% 40% 30% 30% / 40% 40% 25% 25%;
  }

  .services-intro {
    position: absolute; left: 104px; top: 476px;
    font-size: 19px; line-height: 21px;
  }
  .services {
    position: absolute; left: 197px; top: 539px; width: 245px;
    list-style: none; font-size: 18px; line-height: 21px;
  }
  .services li { position: relative; margin-bottom: 5px; }
  .services li::before {
    content: ""; position: absolute; left: -21px; top: 6px;
    width: 10px; height: 10px; background: var(--bullet);
  }

  .quote-box {
    position: absolute; left: 86px; top: 756px; width: 363px; height: 68px;
    background: var(--quote-fill); border-radius: 14px;
    font-family: "Arimo", Arial, sans-serif; font-style: italic; font-weight: 700;
    font-size: 17px; color: var(--quote-text); text-align: center; padding-top: 8px;
  }

  .contact {
    position: absolute; left: 104px; top: 902px;
    font-size: 19px; line-height: 27px; font-style: normal;
  }
  .contact strong { font-weight: 600; margin-left: 6px; }
</style>
</head>
<body>

<section class="flyer-side flyer-side--front">
  <div class="trim-frame"></div>

  <div class="brand">
    <div class="brand__mark"></div>
    <div class="brand__name"><span>FormKeep</span><span>Conservation</span></div>
  </div>

  <h1 class="tagline"><span>Perth’s Most Trusted</span><span>Conservation Service</span></h1>

  <p class="credentials">University trained Conservator with over 20 years’ experience in major galleries and museums.</p>

  <div class="artefact artefact--vase" role="img" aria-label="Photograph of an ancient painted ceramic vase with two handles"></div>
</section>

<section class="flyer-side flyer-side--back">
  <div class="trim-frame"></div>

  <div class="artefact artefact--bust" role="img" aria-label="Photograph of a carved wooden head sculpture in profile"></div>

  <p class="services-intro">Conservation and restoration<br>of objects including:</p>
  <ul class="services">
    <li>Historical items, antiques, ceramics and sculpture</li>
    <li>Custom made display fittings and supports.</li>
    <li>Free advice on storage and display techniques to help preserve your treasured items.</li>
  </ul>

  <div class="quote-box">Offering free quotes in your area on:</div>

  <address class="contact">
    Contact:<strong>Helen Marlowe</strong><br>
    9500 1234 / 0400 555 012<br>
    hello@formkeepconservation.com<br>
    www.formkeepconservation.com
  </address>
</section>

</body>
</html>
```